Web site for a company that sells Pinball machines

We need a website that is an online shopping experience for a Store that sells pinball machines and accessories. The name of the store is called "Bumper Vault Arcade." The store it self has a showroom, but we would also like to have an Internet e-commerce presence. We pinball machines made by Halvern gameworks. You can visit their website and see their current list of machines as well as their website for the machines that we are going to carry in our store. Their website is Halverngameworks.example. I am able to use their machine photos as well as their machine brochure PDF files. I am also able to use their logo on my website two list it as a Halvern Authorized Dealer.
This website design needs to be funky, fun, very technologically oriented and modern. The people buying machines our spending anywhere between $5000 and $15,000 on one machine. These Are high-end buyers who are also usually fairly tech savvy or at least enjoy technology and graphics.
Attachments: I have attached photographs of some of my own machines which may be used in the website. I've also attached some downloaded files from Halvern gameworks.example as well as some of their PDF files for brochures. I will carry all of their current models they have listed under games. Not the archived games. I have included one of their machines called Copperfield Limited edition in my photograph attachments. The rest of the photos are just random pictures that I have taken myself and maybe used to build the site. Lastly I have attached my logo which I am not super crazy about so I will also be posting a contest to redesign this logo. Tons more of my own pinball photos are available.
I would like for people to be able to purchase machines and accessories from the website, but also inform them to our actual showroom.
Updates
Target Market(s)
Target market is 16 to 75. Techy individuals to enjoy gaming technology video animation and Vegas style twinkle
Industry/Entity Type
It Company
Coding
Coded - Design and coding required
Number of Pages Required
3 page
Look and feel

```html
<!DOCTYPE html>
<html lang="en">
<head>
<meta charset="utf-8">
<title>Bumper Vault Arcade – Pinball Machines and Accessories</title>
<link rel="stylesheet" href="https://fonts.googleapis.com/css2?family=Oswald:wght@400;500;600&family=Open+Sans:wght@400;600;700&display=swap">
<style>
:root{
  --ink:#2b2b2b;
  --ink-soft:#555;
  --muted:#8a8a8a;
  --line:#d9d9d9;
  --paper:#ffffff;
  --steel:#4a4a4a;
  --steel-dark:#2e2e2e;
  --night:#18181a;
  --plate-top:#6b6b6b;
  --plate-bot:#353535;
  --star:#f2b01e;
  --neon-pink:#e0206a;
  --neon-orange:#f5902a;
  --neon-violet:#5a2a8a;
  --neon-cyan:#2ab6d8;
  --neon-green:#5ad04a;
}
*{box-sizing:border-box;margin:0;padding:0}
html,body{width:1200px;height:3396px;overflow:hidden}
body{font-family:"Open Sans",Arial,sans-serif;color:var(--ink);background:var(--paper);position:relative}
.section{position:absolute;left:0;width:1200px;overflow:hidden}
.abs{position:absolute}
.heading{font-family:"Oswald",Arial,sans-serif;text-transform:uppercase;letter-spacing:1px}
.plate{position:absolute;left:50%;transform:translateX(-50%);background:linear-gradient(var(--plate-top),var(--plate-bot));color:#fff;font-family:"Oswald",Arial,sans-serif;font-weight:500;font-size:26px;letter-spacing:1px;text-transform:uppercase;padding:6px 40px;border:3px solid #d4d4d4;box-shadow:0 3px 6px rgba(0,0,0,.4);white-space:nowrap}
.btn{display:inline-block;background:linear-gradient(#5a5a5a,#2f2f2f);color:#fff;font-family:"Oswald",Arial,sans-serif;font-size:15px;text-transform:uppercase;letter-spacing:1px;padding:7px 24px;border:1px solid #999;text-decoration:none}
.btn-light{background:linear-gradient(#f6f6f6,#cfcfcf);color:var(--ink);border:1px solid #aaa}
.arrow{position:absolute;width:30px;height:50px}
.stars{color:var(--star);font-size:14px;letter-spacing:2px}

/* header */
.site-header{top:0;height:168px;background:linear-gradient(#ffffff,#e4e4e4);overflow:visible;z-index:5}
.social{left:100px;top:14px;display:flex;gap:8px}
.social span{width:16px;height:16px;background:var(--steel);border-radius:3px;display:block}
.search{left:100px;top:70px;width:260px;height:32px;border:1px solid #bbb;background:#fff;font-size:13px;color:var(--muted);padding:6px 10px}
.search-btn{left:360px;top:70px;width:40px;height:32px;background:var(--steel)}
.utility{left:760px;top:12px;display:flex;gap:26px;font-size:12px;color:var(--ink-soft)}
.phone{left:832px;top:72px;display:flex;align-items:center;gap:8px;font-family:"Oswald",Arial,sans-serif;font-size:20px}
.cart{left:1040px;top:76px;display:flex;align-items:center;gap:6px;font-size:14px}
.main-nav{position:absolute;top:132px;left:0;width:1200px;height:36px;background:linear-gradient(#5a5a5a,#2a2a2a)}
.main-nav a{font-family:"Oswald",Arial,sans-serif;color:#fff;font-size:16px;text-transform:uppercase;text-decoration:none;letter-spacing:1px;position:absolute;top:6px}
.brand{left:490px;top:12px;width:220px;height:220px;border-radius:50%;background:radial-gradient(circle at 50% 35%,#ffffff,#d0d0d0 70%,#a8a8a8);border:5px solid #5e5e5e;display:flex;align-items:center;justify-content:center;z-index:6;box-shadow:0 4px 12px rgba(0,0,0,.5)}
.brand-name{font-family:"Oswald",Arial,sans-serif;font-weight:600;font-size:30px;line-height:1.1;text-align:center;color:var(--steel-dark);text-transform:uppercase}

/* hero */
.hero{top:168px;height:544px}
.hero-art{position:absolute;inset:0;background:
  radial-gradient(ellipse 150px 110px at 600px 150px,rgba(240,236,226,.95),rgba(200,160,170,.3) 70%,transparent),
  radial-gradient(circle 140px at 140px 360px,rgba(90,208,74,.55),transparent),
  radial-gradient(circle 160px at 1060px 120px,rgba(42,182,216,.55),transparent),
  radial-gradient(circle 200px at 900px 430px,rgba(245,144,42,.8),transparent),
  radial-gradient(circle 220px at 300px 120px,rgba(224,32,106,.7),transparent),
  radial-gradient(ellipse 400px 120px at 600px 520px,rgba(255,215,120,.55),transparent),
  linear-gradient(100deg,#2a1240,#8a1a4a 40%,#c85a2a 70%,#2a1a3a)}
.hero-title{position:absolute;top:262px;width:100%;text-align:center;color:#fff;font-size:42px;font-weight:500;text-shadow:0 2px 8px rgba(0,0,0,.8)}
.hero .btn{position:absolute;top:330px;left:546px}

/* perks */
.perks{top:712px;height:108px;background:var(--paper);border-bottom:1px solid var(--line)}
.perk{position:absolute;top:30px;display:flex;gap:12px;align-items:center}
.perk-icon{width:46px;height:46px;border-radius:50%;border:2px solid var(--steel);display:flex;align-items:center;justify-content:center}
.perk h3{font-family:"Oswald",Arial,sans-serif;font-size:18px;font-weight:500;text-transform:uppercase}
.perk p{font-size:12px;color:var(--muted)}

/* about */
.about{top:820px;height:320px;background:linear-gradient(#f6f6f6,#e2e2e2)}
.about .plate{top:44px}
.about-copy{position:absolute;top:128px;left:90px;width:1020px;text-align:center;font-size:15px;line-height:1.75;color:var(--ink-soft)}
.about .btn{position:absolute;top:240px;left:548px;font-size:13px;padding:6px 18px}

/* products */
.products{top:1140px;height:640px;background:
  radial-gradient(circle 260px at 180px 200px,rgba(224,32,106,.35),transparent),
  radial-gradient(circle 260px at 1000px 480px,rgba(42,182,216,.3),transparent),
  radial-gradient(circle 220px at 620px 600px,rgba(245,144,42,.3),transparent),
  linear-gradient(rgba(18,18,20,.86),rgba(18,18,20,.92)),
  linear-gradient(90deg,#4a2a4a,#1f2d3a,#4a3a24)}
.products .plate{top:60px;font-size:24px;transform:none;padding:4px 36px}
.card{position:absolute;top:160px;width:200px}
.card-media{height:180px;background:#fff;border:2px solid #bbb;display:flex;align-items:center;justify-content:center}
.card .stars{text-align:center;margin-top:14px}
.card-name{color:#fff;font-family:"Oswald",Arial,sans-serif;font-weight:500;font-size:15px;text-align:center;margin-top:4px}
.card-price{color:#fff;font-weight:700;font-size:14px;text-align:center}
.card-actions{display:flex;justify-content:center;gap:6px;margin-top:10px}
.card-actions span{background:#ddd;color:var(--ink);font-size:11px;padding:4px 10px;font-weight:600;text-transform:uppercase}
.card-actions i{width:24px;height:24px;border:1px solid #ccc;display:block}
.products .btn{position:absolute;top:560px;left:553px;font-size:13px;padding:6px 18px}

/* reviews */
.reviews{top:1780px;height:548px;background:linear-gradient(#fafafa,#e6e6e6)}
.reviews .plate{top:72px;font-size:24px}
.bubble{position:absolute;background:linear-gradient(#7c7c7c,#565656);color:#fff;border-radius:14px;padding:28px 54px;font-size:15px;line-height:1.55;text-align:center;box-shadow:0 3px 6px rgba(0,0,0,.25)}
.bubble::after{content:"";position:absolute;left:40px;bottom:-22px;border:12px solid transparent;border-top:12px solid #565656;border-left:12px solid #565656}
.q{font-family:Georgia,serif;font-size:40px;position:absolute;line-height:1}
.reviewer{position:absolute;display:flex;gap:14px;align-items:center}
.avatar{width:80px;height:80px;border:3px solid #fff;background:linear-gradient(#cfc8c0,#958f88);box-shadow:0 1px 4px rgba(0,0,0,.35)}
.reviewer h4{font-family:"Oswald",Arial,sans-serif;font-weight:500;font-size:16px;text-transform:uppercase}

/* promo */
.promo{top:2328px;height:432px;background:
  radial-gradient(circle 200px at 820px 60px,rgba(224,32,106,.45),transparent),
  radial-gradient(circle 220px at 1120px 380px,rgba(42,182,216,.35),transparent),
  radial-gradient(circle 180px at 660px 400px,rgba(245,144,42,.35),transparent),
  linear-gradient(90deg,#2a2a2e,#1a1a1e)}
.promo-art{position:absolute;left:0;top:0;width:500px;height:432px;background:linear-gradient(135deg,#8a8a8e,#4a4a4e);clip-path:polygon(0 0,100% 0,80% 100%,0 100%)}
.promo-machine{position:absolute;left:100px;top:40px;width:300px;height:350px;background:
  radial-gradient(circle 60px at 150px 120px,rgba(90,208,74,.6),transparent),
  linear-gradient(160deg,#7a5ab0,#2d2a5e 55%,#d8a030)}
.promo .plate{left:540px;top:80px;transform:none;font-size:24px}
.promo-copy{position:absolute;left:540px;top:150px;width:600px;color:#fff;font-size:18px;line-height:1.5}
.promo .btn{position:absolute;left:540px;top:266px}

/* news */
.news{top:2760px;height:288px;background:var(--paper)}
.news .plate{top:30px;font-size:24px}
.post{position:absolute;top:110px;width:300px;display:flex;gap:14px}
.date{width:80px;height:88px;border:3px solid var(--steel-dark);text-align:center;font-family:"Oswald",Arial,sans-serif;position:relative;flex:none}
.date::before{content:"";position:absolute;left:10px;right:10px;top:-9px;height:6px;border-left:4px solid var(--steel-dark);border-right:4px solid var(--steel-dark)}
.date b{display:block;font-size:28px;font-weight:600;margin-top:8px}
.date span{font-size:16px;text-transform:uppercase}
.post h4{font-family:"Oswald",Arial,sans-serif;font-weight:500;font-size:16px;line-height:1.2;text-transform:uppercase}
.post p{font-size:12px;color:var(--muted);margin-top:6px;line-height:1.45}
.post a{font-size:12px;font-weight:700;color:var(--ink);text-decoration:none;display:block;margin-top:8px}

/* footer */
.site-footer{top:3048px;height:292px;background:var(--steel-dark);color:#ccc}
.col{position:absolute;top:36px;font-size:13px;line-height:2}
.col h5{font-family:"Oswald",Arial,sans-serif;color:#fff;font-size:18px;font-weight:500;text-transform:uppercase;margin-bottom:8px}
.col li{list-style:none}
.signup{left:520px}
.signup p{width:310px;line-height:1.5}
.email{width:310px;height:32px;background:#fff;color:var(--muted);padding:5px 10px;margin-top:10px}
.subscribe{margin-top:12px;background:#666;color:#fff;padding:4px 14px;display:inline-block;line-height:1.6}
.foot-brand{left:900px;top:24px;width:190px;height:190px;border-radius:50%;border:4px solid #777;display:flex;align-items:center;justify-content:center}
.foot-brand span{font-family:"Oswald",Arial,sans-serif;font-weight:600;color:#cfcfcf;font-size:24px;text-align:center;line-height:1.1;text-transform:uppercase}
.cards{position:absolute;left:880px;top:236px;display:flex;gap:8px}
.cards span{width:36px;height:22px;background:#ddd;border-radius:3px;display:block}
.copyright{top:3340px;height:56px;background:#1a1a1a;color:#aaa;font-size:13px;padding:19px 100px}
.chat{position:absolute;right:20px;top:16px;background:#777;color:#fff;font-size:12px;padding:6px 14px}
</style>
</head>
<body>

<header class="section site-header">
  <div class="abs social"><span></span><span></span><span></span></div>
  <div class="abs search">Search</div>
  <div class="abs search-btn">
    <svg width="40" height="32" viewBox="0 0 40 32"><circle cx="19" cy="15" r="6" fill="none" stroke="#fff" stroke-width="2"/><line x1="23" y1="19" x2="27" y2="23" stroke="#fff" stroke-width="2"/></svg>
  </div>
  <nav class="abs utility"><span>My Account</span><span>Track Order</span><span>FAQ</span><span>My Wishlist</span><span>Login</span></nav>
  <div class="abs phone">
    <svg width="24" height="24" viewBox="0 0 24 24"><circle cx="12" cy="12" r="11" fill="var(--steel)"/><path d="M8 6l2 0 1 3-1.5 1a7 7 0 0 0 4 4l1-1.5 3 1v2a2 2 0 0 1-2 1A10 10 0 0 1 7 8a2 2 0 0 1 1-2z" fill="#fff"/></svg>
    123-456-7890
  </div>
  <div class="abs cart">
    <svg width="22" height="20" viewBox="0 0 22 20"><path d="M1 2h4l3 11h10l2-8H6" fill="none" stroke="#333" stroke-width="2"/><circle cx="9" cy="17" r="1.8" fill="#333"/><circle cx="17" cy="17" r="1.8" fill="#333"/></svg>
    $0.00
  </div>
  <nav class="main-nav">
    <a href="#" style="left:100px">Home</a>
    <a href="#" style="left:220px">About Us</a>
    <a href="#" style="left:368px">Product</a>
    <a href="#" style="left:752px">Accessories</a>
    <a href="#" style="left:912px">News</a>
    <a href="#" style="left:1008px">Contact Us</a>
  </nav>
  <div class="abs brand"><span class="brand-name">Bumper<br>Vault<br>Arcade</span></div>
</header>

<section class="section hero">
  <div class="hero-art" role="img" aria-label="Photo of a brightly lit pinball playfield in the showroom"></div>
  <h1 class="hero-title heading">We Sells Pinball Machines and Accessories</h1>
  <a class="btn btn-light" href="#">Shop Now</a>
</section>

<section class="section perks">
  <div class="perk" style="left:100px">
    <div class="perk-icon"><svg width="26" height="18" viewBox="0 0 26 18"><rect x="1" y="2" width="15" height="10" fill="none" stroke="#444" stroke-width="2"/><path d="M16 5h5l4 4v3h-9z" fill="none" stroke="#444" stroke-width="2"/><circle cx="6" cy="15" r="2" fill="#444"/><circle cx="20" cy="15" r="2" fill="#444"/></svg></div>
    <div><h3>Free Shipping &amp; Return</h3><p>Free shipping on all orders over $50</p></div>
  </div>
  <div class="perk" style="left:460px">
    <div class="perk-icon"><svg width="20" height="20" viewBox="0 0 20 20"><text x="10" y="16" text-anchor="middle" font-family="Oswald,sans-serif" font-size="17" fill="#444">$</text></svg></div>
    <div><h3>Money Back Guarantee</h3><p>100% money back guarantee</p></div>
  </div>
  <div class="perk" style="left:860px">
    <div class="perk-icon"><svg width="22" height="22" viewBox="0 0 22 22"><circle cx="11" cy="11" r="8" fill="none" stroke="#444" stroke-width="2"/><path d="M11 6v5l3 3" fill="none" stroke="#444" stroke-width="2"/></svg></div>
    <div><h3>Online Support 24/7</h3><p>Lorem ipsum dolor sit amet</p></div>
  </div>
</section>

<section class="section about">
  <h2 class="plate">About Bumper Vault Arcade</h2>
  <p class="about-copy">Lorem ipsum dolor sit amet consectetuer adipiscing elit, sed diam nonummy nibh euismod tincidunt ut laoreet dolore magna aliquam erat volutpat. Ut wisi enim ad minim veniam, quis nostrud exerci tation ullamcorper suscipit lobortis nisl ut aliquip ex ea commodo consequat. Duis autem vel eum iriure dolor in hendrerit in vulputate velit esse molestie consequat, vel illum dolore eu feugiat nulla facilisis at vero eros et accumsan.</p>
  <a class="btn" href="#">Read More</a>
</section>

<section class="section products">
  <h2 class="plate" style="left:268px">Featured Products</h2>
  <h2 class="plate" style="left:676px">Accessories</h2>
  <svg class="arrow" style="left:30px;top:225px" viewBox="0 0 30 50"><path d="M22 6L8 25l14 19" fill="none" stroke="#fff" stroke-width="4"/></svg>
  <svg class="arrow" style="left:1140px;top:225px" viewBox="0 0 30 50"><path d="M8 6l14 19L8 44" fill="none" stroke="#fff" stroke-width="4"/></svg>

  <article class="card" style="left:100px">
    <div class="card-media"><div role="img" aria-label="Pinball machine cabinet" style="width:100px;height:160px;background:radial-gradient(circle 30px at 50px 40px,rgba(42,182,216,.7),transparent),linear-gradient(160deg,#4a6a9a,#1f2f4a)"></div></div>
    <div class="stars">★★★★★</div><h3 class="card-name">LOREM IPSUM DOLORE</h3><p class="card-price">$10000.00</p>
    <div class="card-actions"><i></i><span>Add to Cart</span><i></i></div>
  </article>
  <article class="card" style="left:368px">
    <div class="card-media"><div role="img" aria-label="Pinball playfield" style="width:110px;height:160px;background:radial-gradient(circle 30px at 55px 110px,rgba(245,144,42,.8),transparent),linear-gradient(160deg,#c2482a,#4a2a6a)"></div></div>
    <div class="stars">★★★★★</div><h3 class="card-name">LOREM IPSUM DOLORE</h3><p class="card-price">$5000.00</p>
    <div class="card-actions"><span>Add to Cart</span></div>
  </article>
  <article class="card" style="left:632px">
    <div class="card-media"><div role="img" aria-label="Pair of pinball flipper bats" style="height:24px;width:150px;border-radius:12px;background:linear-gradient(90deg,#2a8a4a,#6ac070)"></div></div>
    <div class="stars">★★★★★</div><h3 class="card-name">LOREM IPSUM DOLORE</h3><p class="card-price">$500.00</p>
    <div class="card-actions"><span>Add to Cart</span></div>
  </article>
  <article class="card" style="left:896px">
    <div class="card-media"><div role="img" aria-label="Pinball replacement part" style="height:70px;width:150px;background:linear-gradient(90deg,#2a4aa0,#c23a3a)"></div></div>
    <div class="stars">★★★★★</div><h3 class="card-name">LOREM IPSUM DOLORE</h3><p class="card-price">$800.00</p>
    <div class="card-actions"><span>Add to Cart</span></div>
  </article>
  <a class="btn" href="#">View All</a>
</section>

<section class="section reviews">
  <h2 class="plate">Customer Reviews</h2>
  <svg class="arrow" style="left:60px;top:270px" viewBox="0 0 30 50"><path d="M22 6L8 25l14 19" fill="none" stroke="#333" stroke-width="4"/></svg>
  <svg class="arrow" style="left:1110px;top:270px" viewBox="0 0 30 50"><path d="M8 6l14 19L8 44" fill="none" stroke="#333" stroke-width="4"/></svg>

  <blockquote class="bubble" style="left:150px;top:170px;width:420px">
    <span class="q" style="left:18px;top:14px">“</span>
    Lorem ipsum dolor sit amet, consectetuer adipiscing elit, sed diam nonummy nibh euismod tincidunt ut laoreet dolore.
    <span class="q" style="right:20px;bottom:4px">”</span>
  </blockquote>
  <div class="reviewer" style="left:180px;top:370px">
    <div class="avatar" role="img" aria-label="Customer portrait"></div>
    <div><h4>Martin Holloway</h4><div class="stars">★★★★★</div></div>
  </div>

  <blockquote class="bubble" style="left:600px;top:210px;width:460px">
    <span class="q" style="left:18px;top:14px">“</span>
    Lorem ipsum dolor sit amet, consectetuer adipiscing elit, sed diam nonummy nibh euismod tincidunt ut laoreet dolore.
    <span class="q" style="right:20px;bottom:4px">”</span>
  </blockquote>
  <div class="reviewer" style="left:620px;top:420px">
    <div class="avatar" role="img" aria-label="Customer portrait"></div>
    <div><h4>Clara Vance</h4><div class="stars">★★★★★</div></div>
  </div>
</section>

<section class="section promo">
  <div class="promo-art" role="img" aria-label="Dimmed showroom backdrop"></div>
  <div class="promo-machine" role="img" aria-label="Pinball machine cabinet on display"></div>
  <h2 class="plate">Pinball Machines</h2>
  <p class="promo-copy">Lorem ipsum dolor sit amet, consectetuer adipiscing elit, sed diam nonummy nibh euismod tincidunt ut laoreet dolore magna aliquam erat volutpat. Ut wisi enim ad minim.</p>
  <a class="btn btn-light" href="#">Shop Now</a>
</section>

<section class="section news">
  <h2 class="plate">Latest News</h2>
  <svg class="arrow" style="left:40px;top:130px" viewBox="0 0 30 50"><path d="M22 6L8 25l14 19" fill="none" stroke="#333" stroke-width="4"/></svg>
  <svg class="arrow" style="left:1130px;top:130px" viewBox="0 0 30 50"><path d="M8 6l14 19L8 44" fill="none" stroke="#333" stroke-width="4"/></svg>
  <article class="post" style="left:100px">
    <div class="date"><b>25th</b><span>Mar</span></div>
    <div><h4>Lorem ipsum dolor sit am dwectetuer</h4><p>Lorem ipsum dolor sit amet, cons nibh eusmod tincidunt dolore.</p><a href="#">Read More</a></div>
  </article>
  <article class="post" style="left:440px">
    <div class="date"><b>28th</b><span>Mar</span></div>
    <div><h4>Lorem ipsum dolor sit am dwectetuer</h4><p>Lorem ipsum dolor sit amet, cons nibh eusmod tincidunt dolore.</p><a href="#">Read More</a></div>
  </article>
  <article class="post" style="left:788px">
    <div class="date"><b>31th</b><span>Mar</span></div>
    <div><h4>Lorem ipsum dolor sit am dwectetuer</h4><p>Lorem ipsum dolor sit amet, cons nibh eusmod tincidunt dolore.</p><a href="#">Read More</a></div>
  </article>
</section>

<footer class="section site-footer">
  <div class="col" style="left:100px"><h5>My Account</h5><ul><li>About us</li><li>Contact us</li><li>My Account</li><li>Order History</li><li>Advanced search</li><li>Login</li></ul></div>
  <div class="col" style="left:296px"><h5>Information</h5><ul><li>Delivery Information</li><li>Privacy Policy</li><li>Terms &amp; Conditions</li><li>Order Status</li><li>Wish List</li></ul></div>
  <div class="col signup"><h5>Be the First to Know</h5><p>Get all the latest news on events, sales and offers. Sign up for our newsletter today.</p><div class="email">Email Address</div><span class="subscribe">Subscribe</span></div>
  <div class="abs foot-brand"><span>Bumper<br>Vault<br>Arcade</span></div>
  <div class="cards" aria-label="Accepted payment methods"><span></span><span></span><span></span><span></span><span></span></div>
</footer>

<div class="section copyright">Copyright © 2017 BUMPER VAULT ARCADE. All Rights Reserved.<span class="chat">Online – Chat with us</span></div>

</body>
</html>
```